Masterfolien & mehr | Branche Gesundheit | Anschlussaufträge
Tolle Leistung, netter Kontakt, verdienter Gewinner!
Zielgruppe
Sonnquell ist Dienstleister im Bereich 'Betriebliches Gesundheitsmanagement'. Zielgruppe sind Unternehmen zahlreicher Branchen, die die Gesundheit ihrer Mitarbeiter untersuchen und verbessern wollen.
Aufgabenstellung
Bitte möglichst Startfolie, Folie mit Aufzählungen und Text und Folie mit Bild und Text und Kontaktfolie.
Beispieltexte und eine entsprechende Folienansicht habe ich beigefügt, das könnte helfen.
Die Präsentation soll als E-Mail-Anhang im Nachgang eines Akquiseanrufs genutzt werden und über Produkte und Lösungen informieren.
Bitte Farbgebung berücksichtigen. Blau: 90/51/0/0, grau dunkel: 68/51/58/30, grau hell: 40/33/49/1
Schriften: Offen für Vorschläge, möglichst freie Schriften oder klassische Linotype.
Wir würden den Gewinner gern mit weiteren Aufträgen versehen, z.B. die Vorlage mit vorgegebenen Inhalten füllen, Flussdiagramme erstellen, Schaubilder erstellen etc..

```html
<!DOCTYPE html>
<html lang="de">
<head>
<meta charset="utf-8">
<title>Sonnquell – Präsentationsvorlage</title>
<link rel="stylesheet" href="https://fonts.googleapis.com/css2?family=Source+Sans+3:wght@400;600;700&display=swap">
<style>
  :root {
    --blue: #0069b4;
    --grey-dark: #545b57;
    --grey-light: #f2f2f0;
    --card: #ffffff;
    --ink: #1d1d1b;
    --footer-ink: #a9a48f;
    --logo-ink: #474c4a;
  }
  * { box-sizing: border-box; margin: 0; padding: 0; }
  html, body { width: 1200px; height: 2470px; overflow: hidden; background: #fff; }
  body { position: relative; font-family: "Source Sans 3", "Segoe UI", sans-serif; color: var(--ink); }

  .slide { position: absolute; left: 100px; width: 1000px; height: 563px; background: var(--grey-light); overflow: hidden; }

  /* Title slide */
  .title-slide { top: 57px; left: 101px; width: 997px; height: 562px; background: var(--blue); }
  .photo { position: absolute; }
  .photo--kitchen { left: 0; top: 0; width: 483px; height: 562px; background: linear-gradient(160deg, #e9ecef 0%, #dfe3e2 40%, #c9a56e 70%, #d94a2c 100%); }
  .photo--meadow { left: 497px; top: 0; width: 500px; height: 260px; background: linear-gradient(180deg, #5d8fd0 0%, #9fc0e6 55%, #7a9a4c 75%, #4f6e2e 100%); }
  .photo--yoga { left: 497px; top: 274px; width: 500px; height: 288px; background: linear-gradient(120deg, #8d3f86 0%, #b98bb1 40%, #e9e4df 65%, #b8c46a 100%); }
  .title-badge { position: absolute; left: 319px; top: 97px; width: 340px; height: 340px; border-radius: 50%; background: #fff; display: flex; flex-direction: column; align-items: center; justify-content: center; gap: 18px; }
  .brand-dot { width: 70px; height: 70px; border-radius: 50%; background: var(--logo-ink); }
  .brand-name { font-weight: 700; color: var(--logo-ink); font-size: 62px; line-height: 1; }

  /* Shared pieces */
  .ribbon { position: absolute; left: 0; top: 0; width: 1000px; height: 61px; }
  .ribbon-label { position: absolute; left: 0; right: 0; top: 0; height: 61px; text-align: center; line-height: 61px; color: #fff; font-weight: 600; font-size: 31px; letter-spacing: 0.3px; }
  .footer { position: absolute; left: 0; bottom: 0; width: 100%; height: 46px; background: var(--grey-dark); color: var(--footer-ink); font-size: 15px; text-align: center; line-height: 46px; letter-spacing: 0.3px; }
  .card { position: absolute; background: var(--card); border-radius: 8px; }
  .card h3 { font-size: 18px; font-weight: 600; }
  .card p { font-size: 17.5px; line-height: 22.5px; }
  .card h3.accent { color: var(--blue); font-size: 21px; }

  /* Slide 2 */
  .bullets-slide { top: 653px; }
  .text-card { left: 83px; top: 92px; width: 402px; height: 186px; padding: 14px 18px; }
  .text-card h3 { margin-bottom: 20px; }
  .chart { position: absolute; left: 102px; top: 320px; width: 310px; height: 136px; }
  .bullet-card { left: 542px; top: 92px; width: 367px; height: 391px; padding: 16px 24px 0 28px; }
  .bullet-list { list-style: none; }
  .bullet-list li { position: relative; padding-left: 44px; font-size: 17.5px; line-height: 22.5px; }
  .bullet-list li::before { content: ""; position: absolute; left: 0; top: 4px; width: 24px; height: 24px; border-radius: 50%; background: var(--blue); }
  .bullet-list li + li { margin-top: 12px; }
  .bullet-list li.spaced { margin-top: 40px; }

  /* Slide 3 */
  .image-slide { top: 1247px; }
  .photo--runners { left: 511px; top: 62px; width: 489px; height: 455px; background: linear-gradient(170deg, #6b7a2a 0%, #a4651f 35%, #5a4630 65%, #3d3a36 100%); }
  .story-card { left: 76px; top: 93px; width: 400px; height: 374px; padding: 16px 26px; }
  .story-card h3 { margin-bottom: 22px; }
  .story-card p + p { margin-top: 22px; }

  /* Slide 4 */
  .contact-slide { top: 1842px; }
  .contact-card { left: 94px; top: 110px; width: 420px; height: 337px; padding: 20px 24px; text-align: center; }
  .contact-card h3 { margin-bottom: 22px; }
  .contact-card p { font-size: 20px; line-height: 26px; }
  .contact-brand { margin-top: 30px; display: flex; flex-direction: column; align-items: center; gap: 8px; }
  .contact-brand .brand-dot { width: 34px; height: 34px; }
  .contact-brand .brand-name { font-size: 30px; }
  .map { position: absolute; left: 569px; top: 148px; width: 329px; height: 262px; border: 2px solid #555; background: linear-gradient(135deg, #e9e9e7 0%, #efefed 50%, #cfe8c0 80%, #e9e9e7 100%); }
</style>
</head>
<body>

  <section class="slide title-slide">
    <div class="photo photo--kitchen" role="img" aria-label="Foto: Schüssel mit frischem Salat, Gemüse und Messer auf einem Küchenbrett"></div>
    <div class="photo photo--meadow" role="img" aria-label="Foto: Mann im Anzug wirft auf einer grünen Wiese Papiere in die Luft"></div>
    <div class="photo photo--yoga" role="img" aria-label="Foto: Gruppe bei einer Entspannungsübung auf Matten in einem Kursraum"></div>
    <div class="title-badge">
      <span class="brand-dot"></span>
      <span class="brand-name">Sonnquell</span>
    </div>
  </section>

  <section class="slide bullets-slide">
    <svg class="ribbon" viewBox="0 0 1000 61" aria-hidden="true"><path d="M55 0H941L882 52Q872 61 858 61H145Q131 61 121 52Z" fill="var(--blue)"/></svg>
    <h2 class="ribbon-label">HEADLINE</h2>

    <div class="card text-card">
      <h3>Platzhaltertext</h3>
      <p>Cuptam rem solenis quo quia aut quo odig-nam entiur? Qui solupta dessuntum istrum quos arum, te vellorpos quis nam ulparci duci-pie ndaest, qui cum qui occulpa sim fuga. Il int aut experro ipit, omnimil ignatem quae vera</p>
    </div>

    <svg class="chart" viewBox="0 0 310 136" aria-label="Flächendiagramm">
      <path d="M2 136V110Q40 60 75 58Q110 56 160 64Q200 70 230 65Q260 58 280 52V136Z" fill="var(--blue)" stroke="#1d1d1b" stroke-width="2"/>
      <path d="M2 0V134H308" fill="none" stroke="#1d1d1b" stroke-width="3"/>
    </svg>

    <div class="card bullet-card">
      <ul class="bullet-list">
        <li>Uptate adi del milla con pel et en-debist, as net, nonsequunto quia vellandes es sum faccabore es</li>
        <li>Namuscie ndandip itibus que nes-tio. Et as int, et plam res quae qui</li>
        <li class="spaced">Eque aut prendi ommolupiet aut dollam, te susa delessimenis in pa qui officiat id maximpo repu-dandit hit int hilibust anda even-dantus, sitatur?</li>
        <li>Udit di susciistis essunt et, non-sed quis por adi occatquodita</li>
      </ul>
    </div>

    <footer class="footer">WWW.SONNQUELL.DE</footer>
  </section>

  <section class="slide image-slide">
    <div class="photo photo--runners" role="img" aria-label="Foto: drei Personen joggen gemeinsam durch einen herbstlichen Park"></div>
    <svg class="ribbon" viewBox="0 0 1000 61" aria-hidden="true"><path d="M55 0H941L882 52Q872 61 858 61H145Q131 61 121 52Z" fill="var(--blue)"/></svg>
    <h2 class="ribbon-label">HEADLINE</h2>

    <div class="card story-card">
      <h3 class="accent">Platzhaltertext</h3>
      <p>Harum harum id qui ut landipi ssitatur se-cusdae nam, accum quid quamenis arum eossint quatios alis el eaquaectamus repel-lut venimene sapis sunt estiber spicillent, tem dignis sin nim autempe litaspe llauda</p>
      <p>doloresti dolupta denihil imus dolupid quo-dipi duntint ut eictus aliquias asped qui sim dictotaqui que aut ut de nimus veliquatur apedi omnienis doluptat rem ad molores am, sin perum, untis atis aut estis et quodi-tem andus. Odias consequia nia num fugiat.</p>
    </div>

    <footer class="footer">WWW.SONNQUELL.DE</footer>
  </section>

  <section class="slide contact-slide">
    <svg class="ribbon" viewBox="0 0 1000 61" aria-hidden="true"><path d="M55 0H941L882 52Q872 61 858 61H145Q131 61 121 52Z" fill="var(--blue)"/></svg>
    <h2 class="ribbon-label">KONTAKT</h2>

    <div class="card contact-card">
      <h3 class="accent">Platzhaltertext</h3>
      <p>Harum harum id qui ut landipissitatur secusdae nam, accuquid quamenis arum eossint quatios alis el eaquaec-taad molores am, sin perum, untis atis aut estis et quoditem andus.</p>
      <div class="contact-brand">
        <span class="brand-dot"></span>
        <span class="brand-name">Sonnquell</span>
      </div>
    </div>

    <div class="map" role="img" aria-label="Stadtplanausschnitt mit der Lage des Standorts"></div>

    <footer class="footer">WWW.SONNQUELL.DE</footer>
  </section>

</body>
</html>
```